Business Card Design for a Software Startup

We'd like to have a business card design. We already have a logo. Basically what we need is a clean design with name, address, cellphone and phone numbers, e-mail and web site address (front) and a space on the back with our logo with the company name on the right side and some texts on the bottom.
We are a development and consulting company in Brazil with highly qualified team of professionals in Java, iOS and Android development and consulting.

Target Market(s)

CIO, IT managers of mid to big size companies

Industry/Entity Type

Business

```html
<!DOCTYPE html>
<html lang="en">
<head>
<meta charset="utf-8">
<title>QELTORA Business Card</title>
<link rel="stylesheet" href="https://fonts.googleapis.com/css2?family=Questrial&display=swap">
<style>
  :root {
    --stage: #e9e6e1;
    --card-white: #f3f3f3;
    --navy: #15467a;
    --navy-deep: #0f3563;
    --blue-bright: #1590d8;
    --blue-mid: #1a5fb0;
    --blue-edge: #27357a;
    --white: #ffffff;
  }
  * { box-sizing: border-box; margin: 0; padding: 0; }
  html, body { width: 1200px; height: 900px; overflow: hidden; }
  body {
    background: var(--stage);
    font-family: "Questrial", "Century Gothic", sans-serif;
    position: relative;
  }
  .card {
    position: absolute;
    width: 620px;
    height: 360px;
    box-shadow: 0 6px 18px rgba(0,0,0,0.18);
    overflow: hidden;
  }
  /* Front */
  .card-front { left: 140px; top: 60px; background: var(--card-white); }
  .brand {
    position: absolute; left: 60px; top: 152px;
    display: flex; align-items: center; gap: 10px;
    color: var(--navy-deep);
  }
  .brand-square { width: 36px; height: 36px; background: var(--navy); border-radius: 4px; }
  .brand-name { font-size: 36px; letter-spacing: 1px; }
  .name-band {
    position: absolute; left: 318px; top: 130px; width: 302px; height: 64px;
    background: var(--navy); color: var(--white); text-align: center; padding-top: 10px;
  }
  .person-name { font-size: 21px; }
  .person-title { font-size: 11px; margin-top: 2px; }
  .address {
    position: absolute; right: 34px; top: 222px; text-align: right;
    color: var(--navy); font-size: 14px; line-height: 19px; font-style: normal;
  }
  .contact-rule {
    position: absolute; left: 70px; right: 30px; top: 298px; height: 2px;
    background: linear-gradient(to right, rgba(21,70,122,0), var(--navy) 40%, var(--navy) 70%, rgba(21,70,122,0));
  }
  .contact-row {
    position: absolute; left: 110px; top: 310px;
    display: flex; gap: 22px; color: var(--navy); font-size: 15px;
  }
  .contact-item { display: flex; align-items: center; gap: 7px; white-space: nowrap; }
  .contact-item svg { width: 14px; height: 14px; }
  /* Back */
  .card-back {
    left: 440px; top: 480px;
    background: radial-gradient(ellipse at 62% 40%, var(--blue-bright) 0%, var(--blue-mid) 45%, var(--blue-edge) 100%);
  }
  .back-streaks { position: absolute; inset: 0; width: 100%; height: 100%; }
  .back-brand {
    position: absolute; left: 0; right: 0; top: 62px;
    display: flex; flex-direction: column; align-items: center; color: var(--white);
  }
  .back-square { width: 130px; height: 130px; background: var(--white); border-radius: 14px; }
  .back-name { font-size: 44px; letter-spacing: 2px; margin-top: 12px; }
  .back-web {
    position: absolute; left: 0; right: 0; top: 300px; text-align: center;
    color: var(--white); font-size: 15px; letter-spacing: 0.5px;
  }
</style>
</head>
<body>
  <section class="card card-front" aria-label="Business card front">
    <div class="brand">
      <span class="brand-square"></span>
      <span class="brand-name">QELTORA</span>
    </div>
    <div class="name-band">
      <div class="person-name">Marina L Costa</div>
      <div class="person-title">Manager</div>
    </div>
    <address class="address">
      88 harbor lane, suite 210<br>
      lakewood, oregon 54321 - 0000
    </address>
    <div class="contact-rule"></div>
    <div class="contact-row">
      <span class="contact-item">
        <svg viewBox="0 0 14 14"><rect x="3.5" y="1" width="7" height="12" rx="1.5" fill="#15467a"/><rect x="5" y="3" width="4" height="5" fill="#f3f3f3"/></svg>
        555 010 2030 40
      </span>
      <span class="contact-item">
        <svg viewBox="0 0 14 14"><rect x="1" y="3" width="12" height="8" fill="none" stroke="#15467a" stroke-width="1.5"/><path d="M1 3 L7 8 L13 3" fill="none" stroke="#15467a" stroke-width="1.5"/></svg>
        marina@qeltora.com
      </span>
      <span class="contact-item">
        <svg viewBox="0 0 14 14"><circle cx="7" cy="7" r="5.8" fill="none" stroke="#15467a" stroke-width="1.4"/><ellipse cx="7" cy="7" rx="2.4" ry="5.8" fill="none" stroke="#15467a" stroke-width="1.2"/><line x1="1.2" y1="7" x2="12.8" y2="7" stroke="#15467a" stroke-width="1.2"/></svg>
        www.qeltora.com
      </span>
    </div>
  </section>

  <section class="card card-back" aria-label="Business card back">
    <svg class="back-streaks" viewBox="0 0 620 360" preserveAspectRatio="none" aria-hidden="true">
      <polygon points="0,300 620,0 620,40 0,360" fill="#ffffff" opacity="0.07"/>
      <polygon points="0,200 420,0 500,0 0,250" fill="#ffffff" opacity="0.06"/>
      <polygon points="120,360 620,120 620,170 220,360" fill="#ffffff" opacity="0.06"/>
    </svg>
    <div class="back-brand">
      <span class="back-square"></span>
      <span class="back-name">QELTORA</span>
    </div>
    <div class="back-web">www.qeltora.com</div>
  </section>
</body>
</html>
```